Redesign of Quietude Orchard website

- I would like to redesign my ministry website (velno.org)
- Re-brand it with my new logo.

I am looking for something professional and artistic, and focused on creating a good user experience.

The purpose of the site is to:
- Expose TOVKA to the world
- Inform the public about what we are all about.
- Promote my publications (https://www.bookvendra.example/Final-Pilgrim-Leaving-Patterned-Realm-ebook/dp/Q47TX2WK9R/ref=dp_kinw_strp_1)

I don't have to many media material, so I am open to suggestions if the provided images will enhance the look and feel of the site.

Target Market(s)

All English speaking christians , and aspiring Christians around the world.

Industry/Entity Type

Religious

Number of Pages Required

3 page

Font styles to use
Sans Serif

Requirements
Must have
• - Add donation link through CoinDrift
• - A mission page that contains the description found on the "About us" page on Velno.org
• - A personal author page that will include my bio, publication, and contact information. People should be able to email me right from the page
• - Social media links
Nice to have
• - An address book, were people can send us their contact information.

```html
<!DOCTYPE html>
<html lang="en">
<head>
<meta charset="utf-8">
<title>TOVKA – Author Biography</title>
<link href="https://fonts.googleapis.com/css2?family=Roboto:wght@300;400;500;700&family=Open+Sans:wght@400;600;700&display=swap" rel="stylesheet">
<style>
:root{
  --navy:#0f3a5d;
  --navy-deep:#0b2f4c;
  --gold:#f0a814;
  --ink:#4a4a4a;
  --muted:#666666;
  --paper:#ffffff;
  --mist:#f3f3f3;
}
*{box-sizing:border-box;margin:0;padding:0}
html,body{width:1200px;height:2490px;overflow:hidden;background:var(--paper)}
body{position:relative;font-family:"Open Sans",Arial,sans-serif;color:var(--ink)}
h1,h2{font-weight:400}
.abs{position:absolute}

/* header */
.site-header{left:0;top:0;width:1200px;height:120px;background:var(--paper)}
.brand{left:98px;top:44px;display:flex;align-items:center;gap:10px}
.brand-dot{width:16px;height:16px;border-radius:50%;background:var(--gold)}
.brand-name{font-family:"Roboto",Arial,sans-serif;font-weight:500;font-size:44px;color:var(--navy);letter-spacing:1px}
.top-contact{top:24px;display:flex;align-items:center;gap:10px;font-size:15px;color:#555}
.top-contact .ico{width:26px;height:26px;border-radius:50%;background:var(--gold);display:flex;align-items:center;justify-content:center}
.main-nav{left:0;top:77px;width:1200px;height:43px}
.main-nav a{position:absolute;top:0;font-family:"Roboto",Arial,sans-serif;font-size:13.5px;color:var(--navy);text-decoration:none;letter-spacing:.3px}
.main-nav a.active::after{content:"";position:absolute;left:-2px;right:-2px;top:39px;height:3px;background:var(--navy)}
.active-dot{left:828px;top:58px;width:8px;height:8px;border-radius:50%;background:var(--gold)}

/* banner */
.page-banner{left:0;top:120px;width:1200px;height:95px;background:linear-gradient(180deg,#e2b21f,#c99412)}
.page-banner h1{position:absolute;left:0;width:1200px;top:46px;text-align:center;font-family:"Roboto",Arial,sans-serif;font-weight:700;font-size:19px;color:#fff}
.page-banner .rule{left:588px;top:78px;width:24px;height:2px;background:#fff}
.banner-dot{left:594px;top:24px;width:12px;height:12px;border-radius:50%;background:#fff}

/* bio */
.bio{left:0;top:215px;width:1200px;height:540px;background:linear-gradient(180deg,#eceef2,#e4e6ea 60%,#dcdfe3)}
.portrait{left:99px;top:95px;width:365px;height:445px;background:linear-gradient(180deg,#3b3f46,#1f2126)}
.bio-dot{left:486px;top:105px;width:18px;height:18px;border-radius:50%;background:var(--gold)}
.bio-name{left:551px;top:103px;font-family:"Roboto",Arial,sans-serif;font-weight:400;font-size:31px;color:#555;letter-spacing:.5px}
.bio-sub{left:551px;top:142px;font-family:"Roboto",Arial,sans-serif;font-weight:400;font-size:22px;color:#666}
.bio-text{left:481px;top:188px;width:620px;font-size:11.2px;line-height:18.5px;color:var(--muted)}
.bio-text p{margin-bottom:11px}

/* publication */
.book-cover{left:178px;top:838px;width:194px;height:348px;background:linear-gradient(180deg,#3e3a36,#7a5a3e 60%,#a07c52);box-shadow:6px 6px 12px rgba(0,0,0,.25)}
.book-title{left:440px;top:858px;width:600px;font-family:"Roboto",Arial,sans-serif;font-size:32px;line-height:41px;color:var(--navy);font-weight:400}
.stars{left:440px;top:953px;display:flex;gap:2px}
.book-text{left:440px;top:987px;width:590px;font-size:11.2px;line-height:19px;color:var(--muted)}
.book-text p{margin-bottom:12px}
.btn{background:var(--gold);color:#fff;font-family:"Roboto",Arial,sans-serif;text-align:center;border-radius:2px}
.read-more{left:440px;top:1127px;width:108px;height:31px;line-height:31px;font-size:13px}

/* contact info */
.contact-info{left:0;top:1265px;width:1200px;height:495px;background:var(--mist)}
.ci-dot{left:593px;top:70px;width:14px;height:14px;border-radius:50%;background:var(--gold)}
.ci-title{left:0;top:103px;width:1200px;text-align:center;font-family:"Roboto",Arial,sans-serif;font-weight:700;font-size:23px;color:var(--navy)}
.ci-rule{left:580px;top:143px;width:40px;height:2px;background:var(--gold)}
.ci-text{left:244px;top:168px;width:712px;text-align:center;font-size:11px;line-height:18.4px;color:var(--muted)}
.ci-col{top:325px;font-size:12.3px;line-height:21.5px;color:var(--muted)}
.ci-col b{color:#333;font-weight:700}
.ci-badge{top:325px;width:44px;height:44px;border-radius:50%}
.pin-badge{left:140px;border:1.5px solid var(--gold);background:#fff;display:flex;align-items:center;justify-content:center}
.flag-us{left:388px;background:linear-gradient(180deg,#3a4f86 0 45%,#c8303c 45% 100%)}
.flag-cd{left:763px;background:linear-gradient(135deg,#2a8fdc 0 40%,#e2c31c 40% 48%,#c8303c 48% 56%,#e2c31c 56% 64%,#2a8fdc 64%)}

/* quick contact */
.qc-title{left:0;top:1820px;width:1200px;text-align:center;font-family:"Roboto",Arial,sans-serif;font-weight:400;font-size:30px;color:#333}
.qc-label{top:1893px;font-family:"Roboto",Arial,sans-serif;font-weight:500;font-size:14px;color:#333}
.qc-input{top:1927px;height:39px;background:#fff;border:1px solid #e2e2e2}
.send-btn{left:521px;top:1992px;width:158px;height:40px;line-height:40px;font-size:13.5px}

/* footer */
.footer-wave{left:0;top:2100px;width:1200px;height:140px}
.footer-body{left:0;top:2170px;width:1200px;height:320px;background:var(--navy)}
.f-brand{left:98px;top:2148px;display:flex;align-items:center;gap:10px}
.f-brand .brand-name{color:#fff;font-size:40px}
.f-text{color:#fff;font-size:13px;line-height:20px}
.f-head{font-family:"Roboto",Arial,sans-serif;font-weight:500;font-size:16.5px;color:#fff;letter-spacing:.3px}
.f-links{left:444px;top:2225px;list-style:none}
.f-links li{font-size:12.5px;color:#fff;line-height:25.5px;padding-left:18px;position:relative}
.f-links li::before{content:"";position:absolute;left:2px;top:9px;border-left:5px solid #fff;border-top:4px solid transparent;border-bottom:4px solid transparent}
.news-input{left:663px;top:2265px;width:226px;height:40px;background:#fff;font-size:11.5px;color:#777;padding:12px 14px}
.subscribe{left:663px;top:2324px;width:102px;height:40px;line-height:40px;font-size:12px}
.donate{left:781px;top:2322px;width:103px;height:42px;border-radius:6px;background:#f6c24a;color:var(--navy-deep);font-family:"Roboto",Arial,sans-serif;font-weight:700;font-size:15px;text-align:center;line-height:42px}
.social{left:1003px;top:2222px;list-style:none}
.social li{display:flex;align-items:center;gap:9px;height:36.5px;font-size:13.5px;color:#fff}
.social .ring{width:26px;height:26px;border-radius:50%;border:1.5px solid #fff}
.f-rule{left:0;top:2405px;width:1200px;height:1px;background:rgba(255,255,255,.12)}
.copyright{left:0;top:2437px;width:1200px;text-align:center;font-size:12px;color:#fff}
</style>
</head>
<body>

<header class="abs site-header">
  <div class="abs brand"><span class="brand-dot"></span><span class="brand-name">TOVKA</span></div>
  <div class="abs top-contact" style="left:732px">
    <span class="ico"><svg width="13" height="13" viewBox="0 0 24 24"><path fill="#fff" d="M6.6 10.8a15.2 15.2 0 0 0 6.6 6.6l2.2-2.2c.3-.3.7-.4 1-.2 1.1.4 2.3.6 3.6.6.6 0 1 .4 1 1V20c0 .6-.4 1-1 1A17 17 0 0 1 3 4c0-.6.4-1 1-1h3.5c.6 0 1 .4 1 1 0 1.3.2 2.5.6 3.6.1.3 0 .7-.2 1z"/></svg></span>
    <span>555.014.2290</span>
  </div>
  <div class="abs top-contact" style="left:893px">
    <span class="ico"><svg width="13" height="13" viewBox="0 0 24 24"><path fill="#fff" d="M3 5h18v14H3zm2 2v.5l7 4.5 7-4.5V7l-7 4.5z"/></svg></span>
    <span style="font-size:13.5px">rmaronde@quietorchard.org</span>
  </div>
  <span class="abs active-dot"></span>
  <nav class="abs main-nav">
    <a style="left:444px">HOME</a>
    <a style="left:518px">ABOUT US</a>
    <a style="left:619px">MISSION</a>
    <a style="left:706px">AUTHOR</a>
    <a class="active" style="left:792px">PUBLICATIONS</a>
    <a style="left:922px">DONATION</a>
    <a style="left:1024px">CONTACT US</a>
  </nav>
</header>

<section class="abs page-banner">
  <span class="abs banner-dot"></span>
  <h1>BIOGRAPHY</h1>
  <span class="abs rule"></span>
</section>

<section class="abs bio" role="img" aria-label="Faded photograph of a gothic cathedral square behind the biography">
  <div class="abs portrait" role="img" aria-label="Portrait photograph of the author in a dark suit"></div>
  <span class="abs bio-dot"></span>
  <h2 class="abs bio-name">ELIAS MARONDE</h2>
  <div class="abs bio-sub">BIOGRAPHY</div>
  <div class="abs bio-text">
    <p>Elias Maronde is a Bible teacher and missionary of the Gospel of Jesus Christ. He is the president and founder of TOVKA, a missionary organization dedicated to preparing believers for the return of the Lord Jesus Christ. He holds a Bachelor's degree in Computer Science from Northfield Coastal University and has been in ministry for over 15 years. He is married and is a father of 2.</p>
    <p>Elias hopes to show to his generation that:</p>
    <p>Faith and science are not mutually exclusive as many are lead to believe.<br>
    The most important notion about salvation, is the understanding of what we are being saved from.<br>
    Therefore repentance from sin should be at the core of our preaching as noted in Luke 24:45-48.<br>
    The Holy Spirit is still working today as He did back 2000 years ago.</p>
  </div>
</section>

<section>
  <div class="abs book-cover" role="img" aria-label="Book cover showing a lone traveller on a dusty road"></div>
  <h2 class="abs book-title">THE FINAL PILGRIM: LEAVING A PATTERNED REALM EREADER EDITION</h2>
  <div class="abs stars" aria-label="Five stars">
    <svg width="100" height="18" viewBox="0 0 100 18"><g fill="#f0a814">
      <path id="st" d="M9 0l2.6 5.6 6.1.7-4.5 4.2 1.2 6.1L9 13.6 3.6 16.6l1.2-6.1L.3 6.3l6.1-.7z"/>
      <use href="#st" x="20"/><use href="#st" x="40"/><use href="#st" x="60"/><use href="#st" x="80"/></g></svg>
  </div>
  <div class="abs book-text">
    <p>Society has changed faster in the past hundred years than in any other period of human history. This change has profound spiritual implications that most of us are completely unaware of. In a unique way, The Final Pilgrim exposes a conspiracy that starts from the beginning of time to the end of the world.</p>
    <p>It tells how Satan has slowly but surely groomed society to become what it is today, and how he has prepared it for the leadership of the Antichrist in the future.</p>
  </div>
  <div class="abs btn read-more">READ MORE</div>
</section>

<section class="abs contact-info">
  <span class="abs ci-dot"></span>
  <h2 class="abs ci-title">CONTACT INFORMATION</h2>
  <span class="abs ci-rule"></span>
  <p class="abs ci-text">As a missionary organization, in Quietude Orchard we train and equipe, anyone that the Lord Jesus leads to join the mission and many who are just friends and partens but happen to need what we have to offer. Our primary goal is to warn and remind the Church body that the Lord Jesus Christ is about to return. To do so we use every tool at our disposal, and go everywhere the Spirit of God takes us. We do not often plant churches, however; over the years we found that different places have different needs. Therefore as the need presents itself we may just pass through or plant churches as the Holy Spirit leads. If you are seeking to get involved in anyway, please feel free to contact one of the following people to learn more about how you can get involved:</p>
  <div class="abs ci-badge pin-badge"><svg width="14" height="18" viewBox="0 0 14 18"><path fill="#0f3a5d" d="M7 0a7 7 0 0 0-7 7c0 5 7 11 7 11s7-6 7-11a7 7 0 0 0-7-7zm0 9.5A2.5 2.5 0 1 1 7 4.5a2.5 2.5 0 0 1 0 5z"/></svg></div>
  <div class="abs ci-col" style="left:200px">Mailing address:<br>QUIETUDE ORCHARD<br>12 Fenwick Lane<br>Ashbury, Maine 04990<br>USA</div>
  <div class="abs ci-badge flag-us" role="img" aria-label="Round national flag of the United States"></div>
  <div class="abs ci-col" style="left:448px"><b>In the USA:</b><br>Ruth MARONDE: rmaronde@quietorchard.org<br>Ned HALLOWAY: nhalloway27@quietorchard.org</div>
  <div class="abs ci-badge flag-cd" role="img" aria-label="Round national flag of the D.R. Congo"></div>
  <div class="abs ci-col" style="left:823px"><b>In the D.R.Congo:</b><br>Pastor Pascal-Aurel BENZANGA-TOKO:<br>pascal@quietorchard.org<br>Pastor Gaspard LUKENI:<br>gaspard@quietorchard.org</div>
</section>

<section>
  <h2 class="abs qc-title">QUICK CONTACT</h2>
  <label class="abs qc-label" style="left:135px">NAME *</label>
  <label class="abs qc-label" style="left:392px">EMAIL *</label>
  <label class="abs qc-label" style="left:623px">PHONE</label>
  <label class="abs qc-label" style="left:853px">MESSAGE</label>
  <div class="abs qc-input" style="left:133px;width:241px"></div>
  <div class="abs qc-input" style="left:390px;width:215px"></div>
  <div class="abs qc-input" style="left:621px;width:215px"></div>
  <div class="abs qc-input" style="left:852px;width:215px"></div>
  <div class="abs btn send-btn">SEND ENQUIRY</div>
</section>

<footer>
  <svg class="abs footer-wave" viewBox="0 0 1200 140" preserveAspectRatio="none">
    <path d="M0 20 C300 60 700 50 1200 10 L1200 140 L0 140 Z" fill="#0f3a5d"/>
    <path d="M0 16 C300 56 700 46 1200 6" fill="none" stroke="#f0a814" stroke-width="4"/>
  </svg>
  <div class="abs footer-body"></div>

  <div class="abs f-brand"><span class="brand-dot"></span><span class="brand-name">TOVKA</span></div>
  <div class="abs f-head" style="left:98px;top:2210px">CONTACT US</div>
  <div class="abs f-text" style="left:98px;top:2252px">QUIETUDE ORCHARD<br>12 Fenwick Lane Ashbury, Maine 04990 USA</div>
  <div class="abs f-text" style="left:98px;top:2300px;display:flex;gap:18px;align-items:center">
    <svg width="18" height="18" viewBox="0 0 24 24"><path fill="none" stroke="#fff" stroke-width="1.6" d="M6.6 10.8a15.2 15.2 0 0 0 6.6 6.6l2.2-2.2c.3-.3.7-.4 1-.2 1.1.4 2.3.6 3.6.6.6 0 1 .4 1 1V20c0 .6-.4 1-1 1A17 17 0 0 1 3 4c0-.6.4-1 1-1h3.5c.6 0 1 .4 1 1 0 1.3.2 2.5.6 3.6.1.3 0 .7-.2 1z"/></svg>
    <span>Call Us 555.019.7731</span></div>
  <div class="abs f-text" style="left:98px;top:2339px;display:flex;gap:18px">
    <svg width="20" height="16" viewBox="0 0 20 16" style="margin-top:2px"><rect x="1" y="1" width="18" height="14" fill="none" stroke="#fff" stroke-width="1.4"/><path d="M1 2l9 7 9-7" fill="none" stroke="#fff" stroke-width="1.4"/></svg>
    <span>nhalloway27@quietorchard.org<br>rmaronde@quietorchard.org</span></div>

  <div class="abs f-head" style="left:444px;top:2180px">QUICK LINKS</div>
  <ul class="abs f-links"><li>Home</li><li>About us</li><li>Mission</li><li>Author</li><li>Publications</li><li>Contact us</li></ul>

  <div class="abs f-head" style="left:663px;top:2180px">SIGN UP FOR NEWSLETTER</div>
  <div class="abs f-text" style="left:663px;top:2215px;width:240px;font-size:11.5px;line-height:19px">Excepteur sint occaecat cupidatat non proident, sunt in culpa qui</div>
  <div class="abs news-input">Enter Name</div>
  <div class="abs btn subscribe">SUBSCRIBE</div>
  <div class="abs donate">CoinDrift</div>

  <div class="abs f-head" style="left:1003px;top:2180px">SOCIAL</div>
  <ul class="abs social">
    <li><span class="ring"></span>Friendwall</li>
    <li><span class="ring"></span>Chirpline</li>
    <li><span class="ring"></span>Circlenet</li>
    <li><span class="ring"></span>Reelhaven</li>
  </ul>

  <div class="abs f-rule"></div>
  <div class="abs copyright">2016 © Copyrights Velno.All Rights Reserved</div>
</footer>

</body>
</html>
```